Pack - Adventurous, Fun, Exciting, Social Fitness Club needs a Webpage with attitude!

Pack... we're a fun, social, outdoor fitness club that needs not just a homepage designed for our website, but in the process a "personality" for our unique, innovative and cheeky brand.
We pride ourselves on getting our members outdoors trying new, exciting physical activities in an effort to find joy in an active lifestyle, and sharing that experience with other like minded people. We offer:
- Personal Training (1-on-1 Fitness Training)
- Group Fitness Classes (Boxing, Pilates, etc)
- Boot Camps (Military Style - Sandbags, Ropes, Tyres, etc)
- Events (Fun Runs, Triathlons, Ocean Swims, Treks, etc)
- Adventures(Quorra Ridge Trek, Rock Climbing, Kayaking, etc)
Our tag line is 'No Judgements. No Limits!' The homepage should be exciting, adventurous and innovative, illustrating the values of our brand: possibility, thirst for life, personal accomplishment & freedom. It should be fun, friendly & inviting.
A few of our key benefits to members are:
- No Boring Workouts
- No Joining Fees or Long Term Contracts
- Results Guaranteed
The links below should give you a rough idea of the sort of "feel" we're after (vibrant, active, adventurous ).
http://www.campusroamer.com.au/
http://www.layoutgoblin.com/website-templates/31924.html
http://www.layoutgoblin.com/website-templates/32751.html
http://www.velmora.com/
Target Market(s)
Real, Everyday People - Men & Women (30:70) aged mainly between 21-40, who want a more exciting and enjoyable fitness experience than your typical gym offers.
Industry/Entity Type
Fitness
Requirements
Must have
- Strong, uplifting and motivating images of people enjoying fitness/physical activities outdoors

```html
<!DOCTYPE html>
<html lang="en">
<head>
<meta charset="utf-8">
<title>Pack – Social Outdoor Fitness Club</title>
<link rel="stylesheet" href="https://fonts.googleapis.com/css2?family=Anton&family=Fjalla+One&family=Abel&family=Arimo:wght@400;700&display=swap">
<style>
:root{
  --black:#000;
  --body-grey:#333;
  --frame:#dcdcdc;
  --rule:#fff;
  --text-soft:#b5b5b5;
  --text-muted:#999;
  --orange-top:#ffa64a;
  --orange-bottom:#ff7a0a;
  --gold-top:#ffe27a;
  --gold-bottom:#f4a21a;
  --brown:#8a3a00;
  --field:#fde9a6;
  --nav-top:#ffffff;
  --nav-bottom:#c9c9c9;
}
*{box-sizing:border-box;margin:0;padding:0}
html,body{width:1152px;height:1200px;overflow:hidden}
body{position:relative;background:var(--body-grey);font-family:"Arimo",Arial,sans-serif}
.abs{position:absolute}

/* bands */
.header-band{left:0;top:0;width:1152px;height:501px;background:var(--black)}
.header-haze{left:0;top:0;width:560px;height:300px;
  background:radial-gradient(ellipse at 45% 30%,#7d827d 0%,#4a4e4a 30%,#1a1a1a 60%,transparent 80%)}
.band-rule{left:0;width:1152px;height:4px;background:var(--rule)}
.footer-band{left:0;top:1113px;width:1152px;height:87px;background:var(--black)}

/* header */
.login{left:1012px;top:0;width:44px;height:19px;background:#2a2a2a;color:#ddd;font:11px "Arimo",sans-serif;text-align:center;line-height:19px}
.brand{left:104px;top:62px}
.brand-name{font:64px "Anton",sans-serif;color:var(--orange-bottom);letter-spacing:2px;line-height:1}
.tagline{right:96px;top:93px;text-align:right;color:var(--text-muted);font:10.5px/12.5px "Arimo",sans-serif;letter-spacing:.3px}

.main-nav{left:441px;top:151px;width:615px;height:46px;display:flex;background:linear-gradient(var(--nav-top),var(--nav-bottom))}
.main-nav a{display:block;height:46px;line-height:54px;font:24px "Fjalla One",sans-serif;color:#5a5a5a;text-decoration:none;text-align:center;border-right:1px solid #aaa;letter-spacing:-.3px}
.main-nav a span{display:inline-block;transform:scaleX(.88)}
.main-nav a.current{color:#111}
.main-nav a:last-child{border-right:0}

/* hero */
.hero{left:95px;top:197px;width:961px;height:335px;border:5px solid var(--frame);background:#000;overflow:hidden}
.hero-photo{left:0;top:0;width:951px;height:325px;
  background:
    linear-gradient(180deg,rgba(0,0,0,.25),rgba(0,0,0,0) 30%,rgba(0,0,0,.35)),
    linear-gradient(90deg,#3e3a34 0%,#5e594f 20%,#4d4942 45%,#1a1917 52%,#000 55%,#000 86%,#24221e 92%,#4a4640 100%)}
.hero-claim{left:497px;top:132px;display:flex;align-items:center;gap:8px}
.claim-no{font:92px/1 "Abel",sans-serif;color:#7e7e6c;letter-spacing:-3px;-webkit-text-stroke:1.5px #cfcfc4}
.claim-rest{font:37px/37px "Abel",sans-serif;color:#e8e8e8}

/* join bar */
.join-bar{left:161px;top:535px;width:830px;height:59px;border-radius:0 0 8px 8px;
  background:linear-gradient(var(--gold-top),var(--gold-bottom) 60%,#f08c12)}
.join-title{left:39px;top:13px;font:22px "Fjalla One",sans-serif;color:var(--brown);white-space:nowrap;transform:scaleX(.86);transform-origin:left center}
.join-field{top:17px;height:24px;background:var(--field);border:1px solid #d9a335;font:11.5px/22px "Arimo",sans-serif;color:#6b4a1a;padding-left:8px}
.join-btn{left:724px;top:9px;width:71px;height:37px;border-radius:4px;background:linear-gradient(#ffe27a,#f6b326);border:1px solid #d9932a;font:22px/35px "Fjalla One",sans-serif;color:var(--brown);text-align:center}

/* service cards */
.card{top:615px;width:312px;height:217px;border:5px solid var(--frame);border-bottom:0;box-shadow:0 10px 8px -6px #1c1c1c}
.card-photo{width:302px;height:160px}
.card-caption{left:-5px;top:160px;width:312px;height:52px;background:linear-gradient(var(--orange-top),var(--orange-bottom));color:#fff;padding:3px 12px}
.card-title{display:flex;align-items:center;gap:6px;font:23px/26px "Arimo",sans-serif}
.card-sub{font:11.5px "Arimo",sans-serif;margin-top:4px}

/* intro copy */
.intro{left:95px;top:866px;width:628px}
.intro h1{font:bold 25px "Arimo",sans-serif;color:var(--text-muted);margin-bottom:15px}
.intro p{font:11.5px/17.3px "Arimo",sans-serif;color:var(--text-soft);text-align:justify;margin-bottom:17px}

.video-box{left:745px;top:869px;width:311px;height:209px;border:3px solid #d5d5d5;background:var(--body-grey);display:flex;align-items:center;justify-content:center;gap:12px}
.video-box .brand-name{font-size:60px}

/* footer */
.footer-nav{left:95px;top:1141px;font:11px "Arimo",sans-serif;color:#aaa;letter-spacing:.4px}
.footer-nav span{margin:0 7px}
.copyright{left:95px;top:1160px;font:11px "Arimo",sans-serif;color:#aaa;letter-spacing:.4px}
</style>
</head>
<body>
<div class="abs header-band"></div>
<div class="abs header-haze" role="img" aria-label="Smoky grey grunge texture behind the club name"></div>
<div class="abs band-rule" style="top:501px"></div>
<div class="abs band-rule" style="top:1109px"></div>
<div class="abs footer-band"></div>

<div class="abs login">Login</div>
<div class="abs brand"><span class="brand-name">PACK</span></div>
<div class="abs tagline">Pack<br>Lorem Ipsum is simply<br>dummy text of the printing and typesetting industry</div>

<nav class="abs main-nav">
  <a class="current" style="width:89px"><span>Home</span></a>
  <a style="width:105px"><span>About Us</span></a>
  <a style="width:92px"><span>Fitness</span></a>
  <a style="width:208px"><span>Events &amp; Adventures</span></a>
  <a style="width:121px"><span>Contact Us</span></a>
</nav>

<section class="abs hero">
  <div class="abs hero-photo" role="img" aria-label="Man running up weathered stone stairs, seen from behind"></div>
  <div class="abs hero-claim">
    <span class="claim-no">NO</span>
    <span class="claim-rest">JUDGEMENTS.<br>LIMITS!</span>
  </div>
</section>

<form class="abs join-bar">
  <div class="abs join-title">Free Membership, (Valued $65)</div>
  <div class="abs join-field" style="left:310px;width:174px">NAME</div>
  <div class="abs join-field" style="left:493px;width:222px">E-MAIL</div>
  <div class="abs join-btn">Join Us</div>
</form>

<article class="abs card" style="left:95px">
  <div class="card-photo" role="img" aria-label="Trainer guiding a woman through a balance exercise in a bright studio" style="background:linear-gradient(180deg,#d9dcd6 0%,#c8c2b6 45%,#8f8274 100%)"></div>
  <div class="abs card-caption">
    <div class="card-title"><svg width="16" height="18" viewBox="0 0 16 18"><path d="M2 1l9 8-9 8h5l9-8-9-8z" fill="#ffd23a" stroke="#c36a00" stroke-width="1"/></svg>Personal Training</div>
    <div class="card-sub">Free Initial Consult &amp; 1-on-1 Session (valued $80.00)</div>
  </div>
</article>
<article class="abs card" style="left:420px">
  <div class="card-photo" role="img" aria-label="Smiling women training on treadmills in a group class" style="background:linear-gradient(180deg,#e6e0d8 0%,#cdbfb2 50%,#9c8a7b 100%)"></div>
  <div class="abs card-caption">
    <div class="card-title"><svg width="16" height="18" viewBox="0 0 16 18"><path d="M2 1l9 8-9 8h5l9-8-9-8z" fill="#ffd23a" stroke="#c36a00" stroke-width="1"/></svg>Group Fitness</div>
    <div class="card-sub">Intro Pass $25, 7 Days Unlimited Classes</div>
  </div>
</article>
<article class="abs card" style="left:745px">
  <div class="card-photo" role="img" aria-label="Man doing push-ups beside an instructor in camouflage trousers" style="background:linear-gradient(180deg,#d6d4cf 0%,#a49c8a 50%,#5f5848 100%)"></div>
  <div class="abs card-caption">
    <div class="card-title"><svg width="16" height="18" viewBox="0 0 16 18"><path d="M2 1l9 8-9 8h5l9-8-9-8z" fill="#ffd23a" stroke="#c36a00" stroke-width="1"/></svg>Boot Camp</div>
    <div class="card-sub">Coming Soon</div>
  </div>
</article>

<section class="abs intro">
  <h1>Lorem Ipsum</h1>
  <p>is simply dummy text of the printing and typesetting industry. Lorem Ipsum has been the industry's standard dummy text ever since the 1500s, when an unknown printer took a galley of type and scrambled it to make a type specimen book. It has survived not only five centuries, but also the leap into electronic typesetting, remaining essentially unchanged.</p>
  <p>It was popularised in the 1960s with the release of Typesettra sheets containing Lorem Ipsum passages, and more recently with desktop publishing software like Ledgerline PageSmith including versions of Lorem Ipsum. Contrary to popular belief, Lorem Ipsum is not simply random text. It has roots in a piece of classical Latin literature from 45 BC, making it over 2000 years old. Edwin Harlow, a Latin professor at Ashgrove College in Virginia, looked up one of the more obscure Latin words, consectetur, from a Lorem Ipsum passage, and going through the cites of the word in classical literature, discovered the undoubtable source.</p>
</section>

<div class="abs video-box" role="img" aria-label="Club video player">
  <span class="brand-name">PACK</span>
  <svg width="34" height="40" viewBox="0 0 34 40"><path d="M2 2l30 18-30 18z" fill="#eee"/></svg>
</div>

<nav class="abs footer-nav">Home<span>|</span>About Us<span>|</span>Fitness<span>|</span>Events &amp; Adventures<span>|</span>Contact Us<span>|</span>Privacy Statement</nav>
<div class="abs copyright">© 2011 pack. All rights reserved.</div>
</body>
</html>
```